Hedge fund needs power point design for marketing pitch

We need a designer to make our power point pitch more aesthetically appealing to potential clients. We will be marketing our hedge fund to high net worth individuals and financial institutions. The ideal design will look professional and project confidence to our potential clients. We have attached a rough outline of what we have completed so far. We have also attached example cover pages for 2 pitch books produced by our competitors.

Target Market(s)

Financial institutions and wealthy investors

Industry/Entity Type

Finance

Requirements
Must have
• must use our logo and current slides. Must look professional

```html
<!DOCTYPE html>
<html lang="en">
<head>
<meta charset="utf-8">
<title>Aldercrest Capital Management — Pitch Deck Slides</title>
<link rel="stylesheet" href="https://fonts.googleapis.com/css2?family=Tinos:wght@400;700&display=swap">
<style>
  :root {
    --stage-grey: #a9a9a9;
    --page-white: #ffffff;
    --slide-white: #f6f6f6;
    --slide-shade: #e9e9e9;
    --ink: #1b1b1b;
    --forest: #0f4a2c;
    --forest-deep: #0a3a22;
    --emerald: #1f7a4b;
    --gold: #c9a227;
    --rule: #b9b9b9;
    --notch-grey: #a6a6a6;
  }
  * { box-sizing: border-box; margin: 0; padding: 0; }
  html, body { width: 1026px; height: 1200px; overflow: hidden; background: var(--page-white); }
  body { position: relative; font-family: "Tinos", "Times New Roman", serif; color: var(--ink); }

  .stage-band { position: absolute; left: 0; top: 0; width: 1026px; height: 430px; background: var(--stage-grey); }

  .slide { position: absolute; overflow: hidden;
    background: linear-gradient(180deg, var(--page-white) 0%, var(--slide-white) 60%, var(--slide-shade) 100%);
    box-shadow: 2px 4px 8px rgba(0,0,0,.28); }
  .slide--grid { width: 426px; height: 330px; }

  /* Cover slide */
  .cover__panel { position: absolute; left: 0; top: 0; width: 40.4%; height: 100%; }
  .cover__brand { position: absolute; left: 8.7%; top: 45%; color: var(--forest); font-weight: 400;
    text-transform: uppercase; line-height: 1.1; white-space: nowrap; }
  .cover__name { display: block; font-size: 15px; letter-spacing: .1em; }
  .cover__tagline { display: block; font-size: 7.5px; letter-spacing: .05em; }
  .cover__label { position: absolute; left: 8.7%; top: 55.5%; font-size: 13px; line-height: 1.1; }
  .cover__date { display: block; font-size: 10px; }
  .cover__gold { position: absolute; left: 40.4%; top: 0; width: 0.9%; height: 100%; background: var(--gold); }
  .cover__photo { position: absolute; left: 41.3%; top: 0; width: 55.4%; height: 100%;
    background: linear-gradient(180deg, #2f5f9e 0%, #4a7fbd 30%, #7f8fa6 55%, #4b3b43 75%, #2b2b33 100%); }
  .cover__edge { position: absolute; right: 0; top: 0; width: 3.3%; height: 100%; background: var(--forest-deep); }
  .cover--screen { left: 298px; top: 60px; width: 444px; height: 250px; box-shadow: none; }
  .cover--screen .cover__brand { top: 44%; }
  .cover--screen .cover__label { top: 57%; }

  /* Content slides */
  .slide__title { position: absolute; left: 36px; top: 24px; font-size: 21px; font-weight: 400; line-height: 1; }
  .slide__rule { position: absolute; left: 36px; top: 47px; width: 343px; height: 1px; background: var(--rule); }
  .slide__footer { position: absolute; left: 0; bottom: 0; width: 100%; height: 24px;
    background: linear-gradient(180deg, var(--emerald) 0%, var(--forest) 55%, var(--forest-deep) 100%);
    border-top: 1px solid var(--gold); }
  .slide__tab { position: absolute; left: 60px; bottom: 18px; width: 20px; height: 10px; background: var(--notch-grey); }
  .slide__notch { position: absolute; left: 355px; bottom: 17px; width: 0; height: 0;
    border-left: 8px solid transparent; border-right: 8px solid transparent; border-top: 8px solid var(--slide-white); }

  .disclaimer__note { position: absolute; left: 0; top: 88px; width: 100%; text-align: center; font-size: 17px; padding-left: 16px; }
  .disclaimer__visual { position: absolute; left: 24px; top: 114px; width: 355px; height: 172px;
    background: linear-gradient(160deg, #2c6a45 0%, #1a5234 45%, #7c8f84 75%, #d4d6d7 100%); }

  .objective__list { position: absolute; left: 32px; top: 100px; width: 170px; list-style: none; font-size: 9.5px; line-height: 1.2; }
  .objective__item { position: relative; padding-left: 9px; margin-bottom: 24px; }
  .objective__item::before { content: ""; position: absolute; left: 0; top: 3px; width: 5px; height: 5px; border-radius: 50%; background: var(--forest); }
  .objective__sub { display: block; padding-left: 8px; }
  .objective__visual { position: absolute; left: 210px; top: 48px; width: 216px; height: 258px;
    background: radial-gradient(ellipse at 70% 20%, #7fc79d 0%, #2f8a58 35%, #14603a 70%, #0e4b2d 100%); }

  .performance__chart { position: absolute; left: 35px; top: 56px; width: 344px; height: 140px; background: var(--forest); }
  .performance__stats { position: absolute; left: 59px; top: 213px; font-size: 9.5px; line-height: 1.22; }
</style>
</head>
<body>
  <div class="stage-band"></div>

  <section class="slide cover cover--screen">
    <div class="cover__panel">
      <p class="cover__brand"><span class="cover__name">Aldercrest</span><span class="cover__tagline">Capital Management LLC</span></p>
      <p class="cover__label">Confidential<span class="cover__date">April 2016</span></p>
    </div>
    <div class="cover__gold"></div>
    <div class="cover__photo" role="img" aria-label="Night city street with light trails beneath glass towers"></div>
    <div class="cover__edge"></div>
  </section>

  <section class="slide slide--grid cover" style="left:66px; top:452px;">
    <div class="cover__panel">
      <p class="cover__brand"><span class="cover__name">Aldercrest</span><span class="cover__tagline">Capital Management LLC</span></p>
      <p class="cover__label">Confidential<span class="cover__date">April 2016</span></p>
    </div>
    <div class="cover__gold"></div>
    <div class="cover__photo" role="img" aria-label="Night city street with light trails beneath glass towers"></div>
    <div class="cover__edge"></div>
  </section>

  <section class="slide slide--grid disclaimer" style="left:553px; top:452px;">
    <h2 class="slide__title">Disclaimer</h2>
    <div class="slide__rule"></div>
    <p class="disclaimer__note">Get legal counsel on this</p>
    <div class="disclaimer__visual" role="img" aria-label="Laptop showing a green legal screen with a cursor"></div>
    <div class="slide__footer"></div>
    <div class="slide__tab"></div>
    <div class="slide__notch"></div>
  </section>

  <section class="slide slide--grid objective" style="left:66px; top:829px;">
    <h2 class="slide__title">Investment Objective</h2>
    <div class="slide__rule"></div>
    <ul class="objective__list">
      <li class="objective__item">Profit from inefficiencies in equity and index options markets
        <span class="objective__sub">-Buy options that are underpriced</span>
        <span class="objective__sub">-Sell options that are overpriced</span></li>
      <li class="objective__item">Achieve outsized and consistent returns by maintaining a small and nimble fund that can exploit price inefficiencies and move in and out of trades quickly</li>
    </ul>
    <div class="objective__visual" role="img" aria-label="Green rising bar graph with an upward sweeping arrow"></div>
    <div class="slide__footer"></div>
    <div class="slide__tab"></div>
    <div class="slide__notch"></div>
  </section>

  <section class="slide slide--grid performance" style="left:553px; top:829px;">
    <h2 class="slide__title">Simulated Performance</h2>
    <div class="slide__rule"></div>
    <svg class="performance__chart" viewBox="0 0 344 140" aria-label="Simulated return density chart">
      <g fill="#fff" font-family="Tinos, serif">
        <text x="172" y="11" font-size="6" text-anchor="middle">under a more conservative assumed price discount/premium (5%)</text>
        <g font-size="5">
          <text x="48" y="31" text-anchor="end">.03</text>
          <text x="48" y="58" text-anchor="end">.02</text>
          <text x="48" y="84" text-anchor="end">.01</text>
          <text x="48" y="106" text-anchor="end">0</text>
          <text x="279" y="30">.015</text>
          <text x="279" y="56">.001</text>
          <text x="279" y="83">.0005</text>
          <text x="279" y="106">0</text>
          <text transform="translate(40 68) rotate(-90)" text-anchor="middle">Return density Monthly</text>
          <text transform="translate(298 68) rotate(90)" text-anchor="middle">Annual return density</text>
          <text x="226" y="124">Quarterly</text>
          <text x="270" y="124">Yearly</text>
          <text x="226" y="131">Monthly</text>
        </g>
      </g>
      <g stroke="#fff" fill="none">
        <path d="M60 18 V105 H274 V18" stroke-width=".6"/>
        <path d="M60 58 H274 M60 84 H274" stroke-width=".3" opacity=".5"/>
        <path d="M66 104 C120 100 135 60 160 40 C185 22 215 18 235 22 C250 25 256 30 262 35" stroke-width="1.2"/>
        <path d="M66 100 C80 40 88 15 96 18 C104 22 110 80 125 98 C140 104 200 104 262 104" stroke-width=".7" stroke-dasharray="2 1.5"/>
        <path d="M66 103 C80 75 88 48 96 52 C104 56 112 92 128 100 C150 104 200 104 262 104" stroke-width=".7" stroke-dasharray=".8 1"/>
        <path d="M208 122 H222" stroke-width=".6" stroke-dasharray="2 1.5"/>
        <path d="M252 122 H266" stroke-width=".6" stroke-dasharray=".8 1"/>
        <path d="M208 129 H222" stroke-width="1"/>
      </g>
    </svg>
    <p class="performance__stats">
      Mean simulated annual return is 302%<br>
      Only 1% of simulated annual returns are lower than 25.7%<br>
      The mean 3-year and 5-year simulated returns are 6,109% and 96,093%.<br>
      The worst simulated 3-year return out of 10,000 simulated observations is +88%.<br>
      The worst simulated 5-year return out of 10,000 simulated observations is +1,048%.
    </p>
    <div class="slide__footer"></div>
    <div class="slide__tab"></div>
    <div class="slide__notch"></div>
  </section>
</body>
</html>
```